Business Card Design

We need a business card design for a new company. We produce and sell fully grown topiary (please Google topiary pictures if you are not familiar with Topiary).We make many different topiary designs and shapes in all sizes. Ranging from cute little table top animal sculptures such as bunnies and swans for the indoors, to big sculptures such as actual size elephants for outdoor gardens and parks. We also make topiary balls, spiral shapes and other attractive geometrical shapes for indoor and outdoor decorations. We want to see designs that reflects the playfulness and ,liveliness and cute characteristics of our products.Please find attached the logo.Thank you

Industry/Entity Type

Business

Contact Information for Business Card

Company Name : Leaf Forge
Slogan : Shaping Every Garden Bright
Tagline: Topiary...and more
Website : www.leafforge.example

Name on Card : Youssef Nabil Darwish
Title : Founder & CEO
email: youssef_nabil@leafforge.example

Address : 27 El-Masry Street
Ground Floor,Ste.1
El-Marg,Cairo,Egypt

Office Telephone : (02) 25948017
Mobile Number : 01287719462

Requirements
Must have
• The business card must have a white background.

```html
<!DOCTYPE html>
<html lang="en">
<head>
<meta charset="utf-8">
<title>Leaf Forge — Business Card</title>
<link rel="stylesheet" href="https://fonts.googleapis.com/css2?family=Open+Sans:wght@400;600;700&display=swap">
<style>
  :root {
    --backdrop: #ebe7e1;
    --card: #ffffff;
    --green: #6fa14a;
    --green-soft: #c9d8b2;
    --green-pale: #e3ebd6;
    --ink: #2b2b2b;
    --shadow: rgba(60, 40, 20, 0.22);
  }
  * { box-sizing: border-box; margin: 0; padding: 0; }
  html, body {
    width: 1200px; height: 900px; overflow: hidden;
    background: var(--backdrop);
    font-family: "Open Sans", Arial, sans-serif;
  }
  .sheet {
    width: 1200px; height: 900px;
    display: flex; align-items: center; justify-content: center; gap: 50px;
  }
  .card {
    position: relative;
    width: 540px; height: 309px;
    background: var(--card);
    box-shadow: 0 10px 28px var(--shadow);
    overflow: hidden;
  }

  /* Front */
  .card-front {
    display: flex; flex-direction: column; align-items: center; justify-content: center;
  }
  .brand-name {
    color: var(--green);
    font-weight: 600;
    font-size: 50px;
    letter-spacing: 1px;
    line-height: 1;
  }
  .brand-slogan {
    margin-top: 10px;
    color: var(--green);
    font-weight: 600;
    font-size: 15px;
    letter-spacing: 1px;
    padding-bottom: 6px;
    border-bottom: 1.5px solid var(--green);
  }
  .brand-site {
    margin-top: 22px;
    color: var(--green);
    font-size: 17px;
    letter-spacing: 0.5px;
  }

  /* Back */
  .leaf-motif {
    position: absolute; top: 0; right: 0;
    width: 230px; height: 190px;
    background: radial-gradient(ellipse at 60% 55%, var(--green-soft) 0%, var(--green-pale) 60%, rgba(255,255,255,0) 80%);
  }
  .holder {
    position: absolute; left: 34px; top: 118px;
  }
  .holder-name {
    color: var(--green);
    font-weight: 700;
    font-size: 19px;
    letter-spacing: 1.5px;
    text-transform: uppercase;
  }
  .holder-title {
    margin-top: 2px;
    color: var(--ink);
    font-weight: 600;
    font-size: 11px;
  }
  .contact-list {
    list-style: none;
    margin-top: 8px;
    color: var(--ink);
    font-size: 11.5px;
    font-weight: 600;
  }
  .contact-list li {
    display: flex; align-items: flex-start; gap: 5px;
    line-height: 1.45;
  }
  .contact-list .address { margin-top: 10px; }
  .contact-icon { flex: none; width: 12px; height: 12px; margin-top: 3px; }
  .tagline {
    position: absolute; right: 30px; top: 206px;
    color: var(--ink);
    font-weight: 600;
    font-size: 14px;
    letter-spacing: 0.5px;
  }
</style>
</head>
<body>
<main class="sheet">

  <section class="card card-front" aria-label="Card front">
    <div class="brand-name">Leaf Forge</div>
    <div class="brand-slogan">Shaping Every Garden Bright</div>
    <div class="brand-site">www.leafforge.example</div>
  </section>

  <section class="card card-back" aria-label="Card back">
    <div class="leaf-motif" role="img" aria-label="Large pale green leaf-cluster decoration"></div>

    <div class="holder">
      <div class="holder-name">Youssef Nabil Darwish</div>
      <div class="holder-title">Founder &amp; CEO</div>
      <ul class="contact-list">
        <li>
          <svg class="contact-icon" viewBox="0 0 12 12" aria-hidden="true">
            <circle cx="6" cy="6" r="6" fill="#6fa14a"/>
            <path d="M3.8 3.2 L5 3 L5.5 4.6 L4.8 5.2 Q5.5 6.6 6.8 7.2 L7.4 6.5 L9 7 L8.8 8.2 Q5 8.6 3.8 3.2Z" fill="#fff"/>
          </svg>
          (02) 25948017
        </li>
        <li>
          <svg class="contact-icon" viewBox="0 0 12 12" aria-hidden="true">
            <circle cx="6" cy="6" r="6" fill="#6fa14a"/>
            <rect x="4.2" y="2.6" width="3.6" height="6.8" rx="0.7" fill="#fff"/>
            <rect x="4.9" y="3.4" width="2.2" height="4.2" fill="#6fa14a"/>
          </svg>
          01287719462
        </li>
        <li>
          <svg class="contact-icon" viewBox="0 0 12 12" aria-hidden="true">
            <circle cx="6" cy="6" r="6" fill="#6fa14a"/>
            <rect x="3" y="4" width="6" height="4.2" fill="#fff"/>
            <path d="M3 4 L6 6.4 L9 4" fill="none" stroke="#6fa14a" stroke-width="0.8"/>
          </svg>
          youssef_nabil@leafforge.example
        </li>
        <li class="address">
          <svg class="contact-icon" viewBox="0 0 12 12" aria-hidden="true">
            <circle cx="6" cy="6" r="6" fill="#6fa14a"/>
            <path d="M6 2.8 L9.2 5.6 L8.3 5.6 L8.3 8.8 L3.7 8.8 L3.7 5.6 L2.8 5.6Z" fill="#fff"/>
          </svg>
          <span>27 El-Masry Street Ground Floor,<br>Ste.1 El-Marg,Cairo,Egypt</span>
        </li>
      </ul>
    </div>

    <div class="tagline">TOPIARY...AND MORE...</div>
  </section>

</main>
</body>
</html>
```